Brightpath Letterhead

We would like a letterhead for our company. I have uploaded our logo.

Brightpath Ridge Consulting
1450 W Corliss Ave Ste 310
Garland, TX 75041
833-517-2906

```html
<!DOCTYPE html>
<html lang="en">
<head>
<meta charset="utf-8">
<title>Brightpath Letterhead</title>
<link rel="stylesheet" href="https://fonts.googleapis.com/css2?family=Arimo:wght@400&family=Jost:wght@500&family=Mulish:wght@700;800&display=swap">
<style>
  :root {
    --teal: #0b5b6b;
    --mint: #6cc59a;
    --ink: #555559;
    --paper: #fbfbfc;
    --backdrop: #e9e9ea;
  }
  * { margin: 0; padding: 0; box-sizing: border-box; }
  html, body { width: 1200px; height: 1079px; overflow: hidden; }
  body { background: var(--backdrop); position: relative; }

  .letterhead {
    position: absolute; left: 267px; top: 70px;
    width: 665px; height: 939px;
    background: var(--paper);
    overflow: hidden;
    color: var(--ink);
  }

  .brand {
    position: absolute; left: 59px; top: 50px;
    display: flex; align-items: center; gap: 9px;
  }
  .brand-dot { width: 30px; height: 30px; border-radius: 50%; background: var(--teal); flex: none; }
  .brand-name {
    font-family: "Jost", sans-serif; font-weight: 500;
    color: var(--teal); font-size: 17px; line-height: 19px;
    letter-spacing: 2px; text-transform: uppercase;
  }

  .contact {
    position: absolute; right: 60px; top: 52px;
    display: flex; align-items: center;
    font-family: "Arimo", sans-serif; font-size: 10px; line-height: 12.5px;
  }
  .contact-phone { display: flex; align-items: center; gap: 3px; padding-right: 8px; }
  .contact-phone svg { width: 8px; height: 8px; }
  .contact-address { border-left: 1px solid var(--ink); padding: 3px 0 3px 8px; font-style: normal; }

  .salutation {
    position: absolute; left: 60px; top: 289px;
    font-family: "Mulish", sans-serif; font-weight: 800; font-size: 15px;
  }

  .letter-body {
    position: absolute; left: 59px; top: 332px; width: 548px;
    font-family: "Arimo", sans-serif; font-size: 11.1px; line-height: 13.6px;
  }
  .letter-body p { margin-bottom: 12px; }

  .closing {
    position: absolute; left: 60px; top: 615px;
    font-family: "Mulish", sans-serif; font-weight: 700; font-size: 8.5px;
  }
  .signature {
    position: absolute; left: 59px; top: 652px; width: 110px; height: 34px;
    background: linear-gradient(90deg, #e4e4e6, #ededef);
    border-radius: 3px;
  }

  .footer-band {
    position: absolute; left: 0; bottom: 0; width: 590px; height: 20px;
    background: var(--mint);
    clip-path: polygon(0 0, 570px 0, 590px 20px, 0 20px);
  }
  .footer-mark {
    position: absolute; left: 585px; top: 850px;
    width: 90px; height: 90px; border-radius: 50%;
    background: var(--teal);
  }
</style>
</head>
<body>
  <main class="letterhead">
    <header>
      <div class="brand">
        <span class="brand-dot"></span>
        <div class="brand-name">Brightpath Ridge<br>Consulting</div>
      </div>
      <div class="contact">
        <div class="contact-phone">
          <svg viewBox="0 0 24 24" aria-hidden="true"><path fill="#6cc59a" d="M6.6 10.8a15.1 15.1 0 0 0 6.6 6.6l2.2-2.2c.3-.3.7-.4 1-.2 1.1.4 2.3.6 3.6.6.6 0 1 .4 1 1V20c0 .6-.4 1-1 1A17 17 0 0 1 3 4c0-.6.4-1 1-1h3.5c.6 0 1 .4 1 1 0 1.3.2 2.5.6 3.6.1.3 0 .7-.2 1z"/></svg>
          <span>833-517-2906</span>
        </div>
        <address class="contact-address">
          1450 W Corliss Ave<br>Ste 310<br>Garland, TX 75041
        </address>
      </div>
    </header>

    <h1 class="salutation">Dear Mr. Hallworth,</h1>

    <section class="letter-body">
      <p>Lorem ipsum dolor sit amet, consectetuer adipiscing elit, sed diam nonmmy nibh euismod tincidunt ut laor eet dolore magna aliquam erat volutpat. Ut wisi enim ad minim veniam, quis nostrud exerci tationmcorper suscipit lobortis nisl ut aliquip ex ea commodo consequat. Duis autem vel eum iriure dolor in hendrerit in vulputate velit esse molestie consequat, vel illum dolore eu feugiat</p>
      <p>Rorem ipsum dolor sit amet, consectetuer adipiscing elit, sed diam nonmmy nibh euismod tincidunt ut laor eet dolore magna aliquam erat volutpat. Ut wisi enim ad minim veniam, quis nostrud exerci tationmcorper suscipit lobortis nisl ut aliquip ex ea commodo consequat. Duis autem vel eum iriure dolor in hendrerit in vulputate velit esse molest</p>
      <p>Dorem ipsum dolor sit amet, consectetuer adipiscing elit, sed diam nonmmy nibh euismod tincidunt ut laor eet dolore magna aliquam erat volutpat. Ut wisi enim ad minim veniam, quis nostrud exerci tationmcorper suscipit lobortis nisl ut aliquip ex ea commodo consequat. Duis autem vel eum iriure dolor in hendrerit in suscipit lobortis nisl ut aliquip ex ea commodo consequat. Duis autem vel eum iriure dolor in hendrerit in vulputate velit esse molestie consequat, vel illum</p>
      <p>Sorem ipsum dolor sit amet, consectetuer adipiscing elit, sed diam nonmmy nibh euismod tincidunt ut laor eet dolore magna aliquam erat volutpat. Ut wisi enim ad minim veniam, quis nostrud exerci tationmcorper suscipit lobortis nisl ut aliquip ex ea commodo consequat. Duis autem vel eum iriure dolor in</p>
    </section>

    <p class="closing">Sincerely,</p>
    <div class="signature" role="img" aria-label="Handwritten signature of the sender"></div>

    <footer>
      <div class="footer-band"></div>
      <div class="footer-mark"></div>
    </footer>
  </main>
</body>
</html>
```